Orvela Matchmaking - Innovative AI-based Online Dating App

Hello, I am creating a new online dating app that subsumes the personalization and compatibility analysis of human matchmaking, but is combined with the convenience of modern dating apps such as quillet. The app is called Orvela.

There is a lot of pain and fatigue in modern online dating. Orvela uses a concise but effective questionnaire that is combined with cutting-edge AI, social psychology research, and psycholinguistic modelling to effectively and conveniently find dating matches with real compatibility - as opposed to any major app on the market. A personalized introduction for every user is generated everyday to introduce you to a new potential match - this introduction is totally unique and will never be seen before or again. The introduction is intertwined with the user’s images to create an attractive “newsletter” feel.

"Orvela" is Italian for lagoon, which is "a shallow body of water protected from a larger body of water (usually the ocean) by sandbars, barrier islands, or coral reefs." Lagoons are beautiful, tropical, lush watery paradises - as I see it. This is meant to be the inspiration for the feel, color scheme and design of the app.

To that end, I have included concept images of lagoons to evoke the feeling of a paradise getaway where one may meet their soulmate. This is the feeling I would like to convey with the minimalist app design this product needs to compete.

I have included screenshots of the current app UI. There is a screen for
1) potential matches and incoming likes (just like Quillet) with a logo at the top. There are “Like”, “Dislike”, “Super Like”, and “Super Dislike” buttons that float over the screen as it scrolls. These button shape/colors likely need to change to match the rest of the design
2) Overview of message threads with each match
3) View of message threads
4) Settings page

I would like
1) the logo/header image to be redone (as well as the like/dislike/super like/super dislike buttons to be redone to match the new design)
2) icons for the 4 pages in the bottom navigation bar to be redone
3) color scheme to be optimized and evoking of the desired paradise but professional feeling of a hyper-intelligent (but also empathetic) matchmaker
4) design for the settings screen (to look professional and competitive with other dating apps)

The color scheme /layout/spacing/font(s) for the bubbles on the screen where new potential matches are introduced is the most important part of the design I’m looking for. It’s currently a stack of rounded rectangles basically, but I’m open to all ideas to make this app look as professional as possible while conveying the desired elegance, empathy, and uniqueness of the brand.

Thank you!
Updates

Designs look the same

Target Market(s)

Single men and women ages 20 - 45

Industry/Entity Type

Online dating / Matchmaking

Requirements
Must have
• For the main screen where new users are being introduced (i.e. the "swipe" page on most dating apps) - some amount of matchmaking introductory text MUST be shown above the user's first profile picture, as indicated in the current screenshots.
Nice to have
• Re-designs of the top "Orvela" logo/emblem would be nice. If changing the logo, some emblem or graphic in addition to just the text of "Orvela" would be nice. (Like the way "bramcord" has its red flame emblem)
Should not have
• The main "swipe" page should not look identical to other dating apps in the sense of being >90% just a user's first dating profile image. The competitive edge to this app is the user-to-user specific matchmaking introductory text, so some of that must be visible before a user scrolls down for further profile information.

```html
<!DOCTYPE html>
<html lang="en">
<head>
<meta charset="utf-8">
<title>Orvela Matchmaking – App Screens</title>
<link href="https://fonts.googleapis.com/css2?family=Poppins:ital,wght@0,300;0,400;0,500;0,600;1,400&display=swap" rel="stylesheet">
<style>
:root{
  --stage:#3570d4;
  --brand-blue:#1f5fc9;
  --ink:#1d2430;
  --green:#00bd7e;
  --teal:#19a89a;
  --wave-blue:#4f88d8;
  --screen-bg:#eef4fd;
  --white:#ffffff;
  --icon-bg:#dbe6f8;
  --divider:#d7e0ee;
}
*{box-sizing:border-box;margin:0;padding:0}
html,body{width:1200px;height:632px;overflow:hidden}
body{background:var(--stage);font-family:'Poppins',sans-serif;color:var(--ink);position:relative}
.screen{position:absolute;top:32px;width:261px;background:var(--screen-bg);overflow:hidden}
.screen--intro{left:40px;height:533px}
.screen--profile{left:333px;height:533px}
.screen--messages{left:622px;height:446px}
.screen--settings{left:911px;height:446px}

.brand{position:absolute;left:0;right:0;display:flex;align-items:center;justify-content:center;gap:6px;color:var(--brand-blue);font-weight:400;font-size:23px;letter-spacing:1px;z-index:3}
.brand__dot{width:9px;height:9px;border-radius:50%;background:var(--teal)}

/* intro screen */
.intro-header{position:absolute;top:0;left:0;right:0;height:70px;background:var(--white)}
.intro-letter{position:absolute;top:58px;left:0;right:0;height:200px;border-radius:16px 16px 0 0;background:linear-gradient(160deg,#f2f6f8 0%,#e5eef0 45%,#d5e8ea 100%)}
.letter-text{position:absolute;left:8px;right:6px;z-index:2}
.greeting{top:101px;color:var(--brand-blue);font-weight:600;font-size:10px}
.letter-body{top:116px;font-size:8.3px;line-height:14px;text-align:justify}
.intro-photo{position:absolute;top:240px;left:0;right:0;bottom:0;background:linear-gradient(180deg,#6fa9d0 0%,#9cc5d9 35%,#c89d7a 70%,#8b6a50 100%)}
.wave{position:absolute;left:0;width:261px;z-index:2}

.actions{position:absolute;left:0;right:0;display:flex;z-index:3}
.action{position:absolute;border-radius:50%;display:flex;align-items:center;justify-content:center}
.action--solid{width:28px;height:28px;background:var(--white);border:2px solid #b8cdf0}
.action--outline{width:31px;height:31px;background:var(--white);border:2px solid #8fb0e8}
.action svg{width:12px;height:12px}

/* profile screen */
.profile-hero{position:absolute;top:0;left:0;right:0;height:250px;background:linear-gradient(170deg,#f4f7f8 0%,#e4eff1 40%,#cfe6e8 100%)}
.profile-text{position:absolute;left:12px;right:12px;font-size:8.3px;line-height:14.6px;z-index:2}
.signature{color:var(--brand-blue);font-weight:500}
.tags{position:absolute;top:165px;left:12px;display:flex;gap:7px;z-index:2}
.tag{background:var(--green);color:var(--white);font-weight:600;font-size:8.5px;height:25px;padding:0 15px;border-radius:13px;display:flex;align-items:center}
.facts{position:absolute;top:273px;left:12px;right:12px;display:flex;flex-direction:column;gap:8.5px}
.fact{height:25px;background:var(--white);border-radius:13px;display:flex;align-items:center;padding-left:9px;font-size:8.5px}
.fact__label{width:132px;color:var(--brand-blue)}

/* nav */
.nav{position:absolute;left:0;right:0;bottom:0;height:36px;background:var(--green);display:flex;justify-content:space-around;align-items:center;padding:0 12px;z-index:4}
.nav__item{width:24px;height:24px;display:flex;align-items:center;justify-content:center;border-radius:50%}
.nav__item svg{width:16px;height:16px}
.nav__item--active{background:var(--white);width:26px;height:26px}

/* messages & settings */
.page-header{position:absolute;top:0;left:0;right:0;height:104px}
.page-title{position:absolute;top:107px;left:12px;display:flex;align-items:center;gap:12px;font-weight:600;font-size:14.5px}
.page-title svg{width:15px;height:15px}
.card{position:absolute;left:12px;width:237px;height:69px;background:var(--white);border-radius:4px;display:flex;align-items:center;padding-left:10px}
.avatar{width:52px;height:52px;border-radius:3px;flex:none}
.card__body{margin-left:13px;flex:1}
.card__name{color:var(--brand-blue);font-weight:500;font-size:13px;line-height:16px}
.card__text{font-size:8.5px;line-height:14px}
.card__time{color:var(--green);font-style:italic;font-size:8.5px;line-height:16px}
.chevron{width:10px;height:12px;margin-right:14px}
.card__preview{position:absolute;top:15px;right:15px;font-size:8.5px}
.pin-row{display:flex;align-items:center;gap:5px;margin-top:4px}
.pin-row svg{width:7px;height:9px}

.menu{position:absolute;top:220px;left:0;right:0;list-style:none}
.menu__item{height:30.3px;display:flex;align-items:center;padding-left:12px;gap:8px;font-size:8.5px;border-bottom:1px solid var(--divider)}
.menu__item:last-child{border-bottom:none}
.menu__icon{width:21px;height:21px;border-radius:50%;background:var(--icon-bg);display:flex;align-items:center;justify-content:center}
.menu__icon svg{width:9px;height:9px}
</style>
</head>
<body>

<svg width="0" height="0" style="position:absolute">
  <defs>
    <symbol id="i-refresh" viewBox="0 0 24 24"><path d="M19 8a8 8 0 0 0-14 2" fill="none" stroke="currentColor" stroke-width="3" stroke-linecap="round"/><path d="M20 3v6h-6z" fill="currentColor"/><path d="M5 16a8 8 0 0 0 14-2" fill="none" stroke="currentColor" stroke-width="3" stroke-linecap="round"/><path d="M4 21v-6h6z" fill="currentColor"/></symbol>
    <symbol id="i-heart" viewBox="0 0 24 24"><path d="M12 21 3.5 12.6A5.2 5.2 0 0 1 12 5.6a5.2 5.2 0 0 1 8.5 7z" fill="currentColor"/></symbol>
    <symbol id="i-chat" viewBox="0 0 24 24"><path d="M9 3c4.4 0 8 2.6 8 5.8s-3.6 5.8-8 5.8c-.8 0-1.6-.1-2.3-.3L3 16l1-3.2C2.7 11.8 1 10.4 1 8.8 1 5.6 4.6 3 9 3z" fill="currentColor"/><path d="M18.6 9.5c2.7.8 4.4 2.7 4.4 4.8 0 1.4-.8 2.7-2 3.6l.8 3-3.4-1.6c-.8.2-1.6.3-2.4.3-2.6 0-4.8-1-6-2.5 4.5-.2 8.2-3 8.6-7.6z" fill="currentColor"/></symbol>
    <symbol id="i-gear" viewBox="0 0 24 24"><circle cx="12" cy="12" r="8" fill="none" stroke="currentColor" stroke-width="5" stroke-dasharray="3.1 3.2"/><circle cx="12" cy="12" r="7" fill="currentColor"/><circle cx="12" cy="12" r="2.8" fill="var(--green)"/></symbol>
    <symbol id="i-chevron" viewBox="0 0 10 12"><path d="M2 1l6 5-6 5" fill="none" stroke="#333" stroke-width="1.4"/></symbol>
    <symbol id="i-pin" viewBox="0 0 8 10"><path d="M4 0a3.5 3.5 0 0 1 3.5 3.5C7.5 6 4 10 4 10S.5 6 .5 3.5A3.5 3.5 0 0 1 4 0z" fill="#1d2430"/><circle cx="4" cy="3.5" r="1.3" fill="#fff"/></symbol>
  </defs>
</svg>

<!-- Daily introduction screen -->
<section class="screen screen--intro">
  <div class="intro-header"></div>
  <div class="brand" style="top:24px"><span class="brand__dot"></span>Orvela</div>
  <div class="intro-letter" role="img" aria-label="Faint aerial lagoon scene behind the introduction letter"></div>
  <p class="letter-text greeting">Dear Devan,</p>
  <p class="letter-text letter-body">Allow me to introduce you to Marisol, a captivating woman who possesses an enchanting blend of qualities that perfectly align with what you seek in a partner. Her shared interest in creativity is just the beginning of the profound connection you could share. Marisol's passion for games, documentaries, music, and writing mirrors your own, promising endless hours of intellectual stimulation and shared experiences.</p>
  <div class="intro-photo" role="img" aria-label="Profile photo of the introduced match on a beach"></div>
  <svg class="wave" style="top:228px" viewBox="0 0 261 40" height="40"><path d="M0 20 C70 16 120 40 180 34 C220 30 245 18 261 0 V10 C240 30 210 40 180 40 H0z" fill="var(--wave-blue)"/><path d="M0 22 C70 18 120 38 180 36 C220 34 245 22 261 12 V40 H0z" fill="var(--teal)"/><path d="M0 0 H261 C245 18 220 30 180 34 C120 40 70 16 0 20z" fill="#e3eef0"/></svg>
  <div class="action action--solid" style="left:20px;top:468px"><svg viewBox="0 0 12 12"><path d="M2 6h8" stroke="var(--brand-blue)" stroke-width="2.4" stroke-linecap="round"/></svg></div>
  <div class="action action--solid" style="left:81px;top:468px"><svg viewBox="0 0 12 12"><path d="M3 3l6 6M9 3l-6 6" stroke="var(--brand-blue)" stroke-width="2.2" stroke-linecap="round"/></svg></div>
  <div class="action action--solid" style="left:142px;top:468px"><svg viewBox="0 0 24 24" style="color:var(--brand-blue)"><use href="#i-heart"/></svg></div>
  <div class="action action--solid" style="left:202px;top:468px"><svg viewBox="0 0 12 12"><path d="M6 2v8M2 6h8" stroke="var(--brand-blue)" stroke-width="2.2" stroke-linecap="round"/></svg></div>
  <nav class="nav">
    <span class="nav__item"><svg style="color:#fff"><use href="#i-refresh"/></svg></span>
    <span class="nav__item"><svg style="color:#fff"><use href="#i-heart"/></svg></span>
    <span class="nav__item"><svg style="color:#fff"><use href="#i-chat"/></svg></span>
    <span class="nav__item"><svg style="color:#fff"><use href="#i-gear"/></svg></span>
  </nav>
</section>

<!-- Profile details screen -->
<section class="screen screen--profile">
  <div class="profile-hero" role="img" aria-label="Faint aerial lagoon with reef and shoreline"></div>
  <p class="profile-text" style="top:22px;text-align:justify">Partner who not only shares your interests but also complements your desires for adventure and creativity. I encourage you to explore the possibilities that lie within this promising connection.</p>
  <p class="profile-text" style="top:85px">Wishing you the best on this exciting journey of<br>love and companionship.</p>
  <p class="profile-text" style="top:121px">Warm regards,<br><span class="signature">[Your Name]</span></p>
  <div class="tags"><span class="tag">Atheist</span><span class="tag">Liberal</span></div>
  <svg class="wave" style="top:218px" viewBox="0 0 261 40" height="40"><path d="M0 20 C70 16 120 40 180 34 C220 30 245 18 261 0 V10 C240 30 210 40 180 40 H0z" fill="var(--wave-blue)"/><path d="M0 22 C70 18 120 38 180 36 C220 34 245 22 261 12 V24 C240 32 210 40 180 40 H0z" fill="var(--teal)"/><path d="M0 30 C70 26 120 42 180 40 C215 39 240 30 261 22 V40 H0z" fill="var(--screen-bg)"/></svg>
  <div class="facts">
    <div class="fact"><span class="fact__label">Children</span>Have children</div>
    <div class="fact"><span class="fact__label">Family Goals</span>Open to children</div>
    <div class="fact"><span class="fact__label">Diet</span>Omnivore</div>
    <div class="fact"><span class="fact__label">Drinking</span>Rarely</div>
    <div class="fact"><span class="fact__label">Drugs</span>Recently</div>
  </div>
  <div class="action action--outline" style="left:25px;top:456px"><svg viewBox="0 0 12 12"><path d="M2 6h8" stroke="var(--brand-blue)" stroke-width="2.4" stroke-linecap="round"/></svg></div>
  <div class="action action--outline" style="left:87px;top:456px"><svg viewBox="0 0 12 12"><path d="M3 3l6 6M9 3l-6 6" stroke="var(--brand-blue)" stroke-width="2.2" stroke-linecap="round"/></svg></div>
  <div class="action action--outline" style="left:150px;top:456px"><svg viewBox="0 0 24 24" style="color:var(--brand-blue)"><use href="#i-heart"/></svg></div>
  <div class="action action--outline" style="left:213px;top:456px"><svg viewBox="0 0 12 12"><path d="M6 2v8M2 6h8" stroke="var(--brand-blue)" stroke-width="2.2" stroke-linecap="round"/></svg></div>
  <nav class="nav">
    <span class="nav__item"><svg style="color:#fff"><use href="#i-refresh"/></svg></span>
    <span class="nav__item"><svg style="color:#fff"><use href="#i-heart"/></svg></span>
    <span class="nav__item"><svg style="color:#fff"><use href="#i-chat"/></svg></span>
    <span class="nav__item"><svg style="color:#fff"><use href="#i-gear"/></svg></span>
  </nav>
</section>

<!-- Messages screen -->
<section class="screen screen--messages">
  <svg class="page-header" viewBox="0 0 261 104" width="261" height="104"><path d="M0 0H261V65C240 80 215 100 175 98 C120 94 70 70 0 90z" fill="var(--wave-blue)"/><path d="M0 0H261V80C235 92 210 102 175 102 C120 100 70 76 0 92z" fill="var(--teal)" opacity="0"/><path d="M0 0H261V64C235 86 210 98 175 98 C120 94 70 72 0 88z" fill="var(--teal)"/><path d="M0 0H261V64C235 82 210 94 175 93 C120 90 70 74 0 80z" fill="var(--white)"/></svg>
  <div class="brand" style="top:22px"><span class="brand__dot"></span>Orvela</div>
  <h2 class="page-title"><svg viewBox="0 0 16 16"><rect x="1" y="3" width="14" height="10" rx="1.5" fill="none" stroke="var(--green)" stroke-width="1.6"/><path d="M1.5 4l6.5 5 6.5-5" fill="none" stroke="var(--green)" stroke-width="1.6"/></svg>Messages</h2>
  <div class="card" style="top:143px">
    <div class="avatar" role="img" aria-label="Profile photo of Celia" style="background:linear-gradient(160deg,#7a5a48,#c89a82 55%,#e8e2de)"></div>
    <div class="card__body"><div class="card__name">Celia</div><div class="card__text">Omg you are stunning</div><div class="card__time">12:38 pm</div></div>
    <svg class="chevron"><use href="#i-chevron"/></svg>
  </div>
  <div class="card" style="top:223px">
    <div class="avatar" role="img" aria-label="Profile photo of Rowena" style="background:linear-gradient(160deg,#4c5a48,#d9b49a 50%,#56633f)"></div>
    <div class="card__body"><div class="card__name">Rowena</div><div class="card__text">Oh hi babe.</div><div class="card__time">12:38 pm</div></div>
    <svg class="chevron"><use href="#i-chevron"/></svg>
  </div>
  <div class="card" style="top:302px">
    <div class="avatar" role="img" aria-label="Profile photo of Tomiko, a holiday tree" style="background:linear-gradient(160deg,#b8b4ac,#3e5638 55%,#22301f)"></div>
    <div class="card__body"><div class="card__name">Tomiko</div><div class="card__text">Yo have we spoke yet</div><div class="card__time">12:38 pm</div></div>
    <svg class="chevron"><use href="#i-chevron"/></svg>
  </div>
  <nav class="nav">
    <span class="nav__item"><svg style="color:#fff"><use href="#i-refresh"/></svg></span>
    <span class="nav__item"><svg style="color:#fff"><use href="#i-heart"/></svg></span>
    <span class="nav__item nav__item--active"><svg style="color:var(--brand-blue)"><use href="#i-chat"/></svg></span>
    <span class="nav__item"><svg style="color:#fff"><use href="#i-gear"/></svg></span>
  </nav>
</section>

<!-- Settings screen -->
<section class="screen screen--settings">
  <svg class="page-header" viewBox="0 0 261 104" width="261" height="104"><path d="M0 0H261V65C240 80 215 100 175 98 C120 94 70 70 0 90z" fill="var(--wave-blue)"/><path d="M0 0H261V64C235 86 210 98 175 98 C120 94 70 72 0 88z" fill="var(--teal)"/><path d="M0 0H261V64C235 82 210 94 175 93 C120 90 70 74 0 80z" fill="var(--white)"/></svg>
  <div class="brand" style="top:22px"><span class="brand__dot"></span>Orvela</div>
  <h2 class="page-title"><svg viewBox="0 0 24 24" style="color:var(--green)"><use href="#i-gear"/></svg>Settings</h2>
  <div class="card" style="top:143px">
    <div class="avatar" role="img" aria-label="Own profile photo" style="background:linear-gradient(160deg,#7a5a48,#c89a82 55%,#e8e2de)"></div>
    <div class="card__body"><div class="card__name" style="font-size:11px">Edit Photo</div><div class="pin-row"><svg><use href="#i-pin"/></svg><span class="card__time">Change Location</span></div></div>
    <span class="card__preview">Preview</span>
  </div>
  <ul class="menu">
    <li class="menu__item"><span class="menu__icon"><svg viewBox="0 0 10 10"><circle cx="5" cy="3" r="2.2" fill="var(--brand-blue)"/><path d="M1 10a4 3.5 0 0 1 8 0z" fill="var(--brand-blue)"/></svg></span>Profile (Public)</li>
    <li class="menu__item"><span class="menu__icon"><svg viewBox="0 0 10 10"><rect x="1.5" y="4.5" width="7" height="5" rx="1" fill="var(--brand-blue)"/><path d="M3 4.5V3a2 2 0 0 1 4 0v1.5" fill="none" stroke="var(--brand-blue)" stroke-width="1.3"/></svg></span>Matchmaking Information (Private)</li>
    <li class="menu__item"><span class="menu__icon"><svg viewBox="0 0 10 10"><path d="M2 0h4l2 2v8H2z" fill="var(--brand-blue)"/><path d="M3.5 5h3M3.5 7h3" stroke="#fff" stroke-width=".8"/></svg></span>Privacy Policy</li>
    <li class="menu__item"><span class="menu__icon"><svg viewBox="0 0 10 10"><path d="M7 1l2 2-5.5 5.5L1 9l.5-2.5z" fill="var(--brand-blue)"/></svg></span>Send Feedback</li>
    <li class="menu__item"><span class="menu__icon"><svg viewBox="0 0 10 10"><rect x="1.5" y="1.5" width="7" height="5" fill="none" stroke="var(--brand-blue)" stroke-width="1.2"/><path d="M0 8.5h10" stroke="var(--brand-blue)" stroke-width="1.4"/></svg></span>Preview</li>
    <li class="menu__item"><span class="menu__icon"><svg viewBox="0 0 10 10"><path d="M4 2H1.5v6H4" fill="none" stroke="var(--brand-blue)" stroke-width="1.2"/><path d="M4 5h4M6.5 3l2 2-2 2" fill="none" stroke="var(--brand-blue)" stroke-width="1.3"/></svg></span>Log out</li>
  </ul>
  <nav class="nav">
    <span class="nav__item"><svg style="color:#fff"><use href="#i-refresh"/></svg></span>
    <span class="nav__item"><svg style="color:#fff"><use href="#i-heart"/></svg></span>
    <span class="nav__item"><svg style="color:#fff"><use href="#i-chat"/></svg></span>
    <span class="nav__item nav__item--active"><svg viewBox="0 0 24 24" style="color:var(--brand-blue)"><circle cx="12" cy="12" r="8" fill="none" stroke="currentColor" stroke-width="5" stroke-dasharray="3.1 3.2"/><circle cx="12" cy="12" r="7" fill="currentColor"/><circle cx="12" cy="12" r="2.8" fill="#fff"/></svg></span>
  </nav>
</section>

</body>
</html>
```